I need a business card design to compliment my existing branding [website and book give clear guidance here]. I teach business owners and managers how to become pioneers of business innovation in their industry - to challenge the paradigms and make their competition irrelevant. They will never look at business in the same way again.

The brand stands for innovation - to intelligently challenge the paradigms of each industry and seek to cause disruption. It's as provocative as it is progressive and many clients say that they find it quite uncomfortable to start with - they grow to love it and feel liberated by it.

The astronaut is the leading theme as it represents the pioneer, the maverick, the progressive ones. The astronaut can be as per the logo i.e. with the circle etc. or, can be extracted and used in isolation.

The word 'Masterclass' should not be used on the business card [even though it's in the attached logo].

Target Market(s)

Small to medium business owners, entrepreneurs, 'hungry' employees who want to accelerate their career

Industry/Entity Type

Business

Contact Information for Business Card

You. Pioneering Business Innovation.

Ned Farrow
Chief Innovation Coach

+61 [0]491 570 006
ned.farrow@coppermethodfinches.com
coppermethodfinches.com

Font styles to use
Other font styles liked:
• Eurostile

Requirements
Must have
• Simplistic and elegant is welcome.
• Colours and design must compliment the brand as per the attached documents - the book is probably the best guide as it is handed out at the same time as the business cards [whereas the website is looked at in isolation].
• I find the red stripe across the book cover quite striking.
• Font is Eurostile
Nice to have
• Unusual and eye catching but simple
Should not have
• No space scene in the background [i.e. it should not mimic the website banner]
• Other fonts than Eurostile

```html
<!DOCTYPE html>
<html lang="en">
<head>
<meta charset="utf-8">
<title>Copper Method Finches — Business Card</title>
<link href="https://fonts.googleapis.com/css2?family=Michroma&family=Exo+2:wght@400;500&display=swap" rel="stylesheet">
<style>
  :root {
    --backdrop: #2b2b2d;
    --navy: #0f2a40;
    --coral: #ee6a66;
    --sun: #f7d774;
    --paper: #ffffff;
    --ink: #12304a;
    --soft-line: #6a5a6e;
  }
  * { box-sizing: border-box; margin: 0; padding: 0; }
  html, body { width: 1200px; height: 880px; overflow: hidden; }
  body {
    background: var(--backdrop);
    display: flex; flex-direction: column; align-items: center; justify-content: center;
    gap: 36px;
    font-family: "Exo 2", "Helvetica Neue", sans-serif;
  }
  .card {
    width: 700px; height: 400px; border-radius: 22px;
    position: relative; overflow: hidden;
  }
  .card--front { background: var(--paper); color: var(--ink); }
  .card--back { background: var(--navy); color: var(--paper); }

  .brand { display: flex; flex-direction: column; align-items: center; }
  .brand__mark { width: 118px; height: 118px; border-radius: 50%; }
  .brand__name {
    font-family: "Michroma", "Arial", sans-serif;
    font-size: 19px; letter-spacing: 1px; text-align: center; line-height: 1.35;
    margin-top: 16px; text-transform: uppercase;
  }
  .card--front .brand { position: absolute; left: 0; right: 0; top: 90px; }
  .card--front .brand__mark { background: var(--navy); }
  .card--front .brand__name { color: var(--ink); }
  .front__web {
    position: absolute; left: 0; right: 0; bottom: 62px;
    text-align: center; font-size: 15px; letter-spacing: 1px; color: var(--ink);
  }

  .card--back .brand { position: absolute; left: 70px; top: 80px; width: 250px; }
  .card--back .brand__mark { background: var(--paper); }
  .card--back .brand__name { color: var(--paper); font-size: 17px; }

  .divider {
    position: absolute; left: 340px; top: 100px; width: 1px; height: 200px;
    background: var(--soft-line);
  }
  .person { position: absolute; left: 375px; top: 120px; }
  .person__name {
    font-family: "Michroma", "Arial", sans-serif; font-size: 20px; text-transform: uppercase;
  }
  .person__role { color: var(--coral); font-size: 15px; margin-top: 2px; }
  .contacts { position: absolute; left: 375px; top: 212px; list-style: none; }
  .contacts li { display: flex; align-items: center; gap: 10px; font-size: 14px; margin-bottom: 8px; }
  .contacts svg { width: 20px; height: 20px; flex: none; }

  .planet { position: absolute; }
  .planet--low { left: -70px; bottom: -70px; width: 170px; height: 170px; }
  .planet--high { right: -50px; top: -30px; width: 110px; height: 110px; }
  .comet { position: absolute; width: 28px; height: 20px; }
  .comet--left { left: 36px; top: 215px; }
  .comet--right { right: 70px; top: 160px; }
</style>
</head>
<body>

<section class="card card--front">
  <div class="brand">
    <div class="brand__mark" role="img" aria-label="Brand emblem area"></div>
    <p class="brand__name">Copper Method<br>Finches</p>
  </div>
  <p class="front__web">coppermethodfinches.com</p>
</section>

<section class="card card--back">
  <svg class="planet planet--low" viewBox="0 0 170 170" role="img" aria-label="Striped coral planet illustration">
    <circle cx="85" cy="85" r="85" fill="var(--coral)"/>
  </svg>
  <svg class="planet planet--high" viewBox="0 0 110 110" role="img" aria-label="Striped coral planet illustration">
    <circle cx="55" cy="55" r="55" fill="var(--coral)"/>
  </svg>
  <svg class="comet comet--left" viewBox="0 0 28 20" role="img" aria-label="Small comet illustration">
    <circle cx="18" cy="10" r="9" fill="var(--sun)"/>
  </svg>
  <svg class="comet comet--right" viewBox="0 0 28 20" role="img" aria-label="Small comet illustration">
    <circle cx="18" cy="10" r="9" fill="var(--sun)"/>
  </svg>

  <div class="brand">
    <div class="brand__mark" role="img" aria-label="Brand emblem area"></div>
    <p class="brand__name">Copper Method<br>Finches</p>
  </div>

  <div class="divider"></div>

  <div class="person">
    <p class="person__name">Ned Farrow</p>
    <p class="person__role">Chief Innovation Coach</p>
  </div>

  <ul class="contacts">
    <li>
      <svg viewBox="0 0 20 20" aria-hidden="true"><circle cx="10" cy="10" r="10" fill="var(--coral)"/><path d="M6.5 5.5l2 0 1 2.5-1.3 1a6 6 0 0 0 2.8 2.8l1-1.3 2.5 1v2a1.5 1.5 0 0 1-1.5 1.5A8 8 0 0 1 5 7a1.5 1.5 0 0 1 1.5-1.5z" fill="var(--navy)"/></svg>
      +61 [0]491 570 006
    </li>
    <li>
      <svg viewBox="0 0 20 20" aria-hidden="true"><circle cx="10" cy="10" r="10" fill="var(--coral)"/><rect x="5" y="6.5" width="10" height="7" rx="1" fill="var(--navy)"/><path d="M5.5 7l4.5 3.5L14.5 7" stroke="var(--coral)" fill="none"/></svg>
      ned.farrow@coppermethodfinches.com
    </li>
    <li>
      <svg viewBox="0 0 20 20" aria-hidden="true"><circle cx="10" cy="10" r="10" fill="var(--coral)"/><circle cx="10" cy="10" r="5" fill="none" stroke="var(--navy)" stroke-width="1.3"/><path d="M5 10h10M10 5c-2.5 3-2.5 7 0 10M10 5c2.5 3 2.5 7 0 10" fill="none" stroke="var(--navy)" stroke-width="1.1"/></svg>
      coppermethodfinches.com
    </li>
  </ul>
</section>

</body>
</html>
```